Marlo Tidy Yard Website

We need a website design for this new company. I've attached the company logo. This company is in the construction industry that provides general labor, maintenance and cleaning for construction sites. We want a clean and simple website that can be easy to navigate.

Target Market(s)

Construction industry

Industry/Entity Type

Construction

Number of Pages Required

2 page

Font styles to use
Sans Serif

```html
<!DOCTYPE html>
<html lang="en">
<head>
<meta charset="utf-8">
<title>Marlo Tidy Yard</title>
<link href="https://fonts.googleapis.com/css2?family=Montserrat:wght@400;600;700;800&family=Open+Sans:wght@400;600;700&display=swap" rel="stylesheet">
<style>
:root{
  --navy:#1a1478;
  --navy-deep:#130f5e;
  --nav-active:#2d28c8;
  --orange:#f26a12;
  --ink:#1d1d2b;
  --text:#555a66;
  --muted:#8a8f99;
  --mint:#eef7f0;
  --line:#dcdfe6;
  --white:#ffffff;
  --black:#050505;
}
*{box-sizing:border-box;margin:0;padding:0}
html,body{width:1200px;height:3558px;overflow:hidden}
body{position:relative;background:var(--white);font-family:"Open Sans",Arial,sans-serif;color:var(--text)}
.abs{position:absolute}
h2.section-title{font-family:"Montserrat",Arial,sans-serif;font-weight:400;font-size:23px;letter-spacing:1px;text-transform:uppercase;text-align:center;color:var(--ink)}
h2.section-title b{font-weight:700}

/* header */
.topbar{left:0;top:0;width:1200px;height:75px;background:var(--white)}
.brand{left:137px;top:12px;display:flex;align-items:center;gap:10px}
.brand-mark{width:18px;height:18px;background:var(--orange)}
.brand-name{font-family:"Montserrat",Arial,sans-serif;font-weight:800;font-size:22px;color:var(--navy);letter-spacing:.3px;line-height:50px}
.contact-top{top:26px;display:flex;align-items:center;gap:10px;font-size:13px;color:var(--ink);font-weight:600}
.contact-top .ico{width:24px;height:24px;border-radius:50%;background:var(--navy);display:flex;align-items:center;justify-content:center}
.nav{left:0;top:75px;width:1200px;height:40px;background:var(--navy-deep)}
.nav ul{list-style:none;display:flex;margin-left:132px;height:40px}
.nav li{font-family:"Montserrat",Arial,sans-serif;font-weight:700;font-size:12px;color:var(--white);padding:0 24px;line-height:40px;text-transform:uppercase}
.nav li.active{background:var(--nav-active)}

/* hero */
.hero{left:0;top:115px;width:1200px;height:510px;background:linear-gradient(90deg,#eae6e0 0%,#ddd6cc 40%,#c9b9a4 65%,#d7a94a 85%,#a3907a 100%)}
.hero-title{left:132px;top:145px;font-family:"Montserrat",Arial,sans-serif;font-weight:800;font-size:31px;line-height:38px;color:var(--black);text-transform:uppercase}
.hero-sub{left:132px;top:238px;width:340px;font-size:14px;line-height:22px;color:var(--ink);font-weight:600}
.btn{background:var(--orange);color:var(--white);font-family:"Montserrat",Arial,sans-serif;font-weight:700;font-size:12px;text-transform:uppercase;display:flex;align-items:center;justify-content:center}
.hero-btn{left:132px;top:307px;width:162px;height:40px;border-radius:20px}
.hero-arrow{left:56px;top:192px;width:32px;height:32px;border-radius:50%;background:rgba(0,0,0,.35)}
.hero-curve{left:0;top:515px;width:1200px;height:115px}

/* about */
.about-title{left:137px;top:710px;font-family:"Montserrat",Arial,sans-serif;font-size:20px;color:var(--ink);letter-spacing:1px}
.about-title b{color:var(--navy);font-weight:700}
.about-text{left:137px;top:755px;width:585px;font-size:12px;line-height:20px}
.about-text p{margin-bottom:14px}
.photo-circle{border-radius:50%;border:6px solid var(--white)}
.about-photo-lg{left:772px;top:710px;width:274px;height:274px;background:radial-gradient(circle at 40% 40%,#e6e3df,#b7b2ab)}
.about-photo-sm{left:706px;top:826px;width:208px;height:208px;background:radial-gradient(circle at 50% 40%,#dfe6ef,#c6c94e 70%,#9ca3ad)}

/* services */
.services{left:0;top:1088px;width:1200px;height:542px;background:var(--navy)}
.services h2.section-title{color:var(--white);position:absolute;top:62px;width:1200px}
.services-desc{position:absolute;top:98px;left:380px;width:440px;text-align:center;color:var(--white);font-size:12px;line-height:18px}
.service{position:absolute;top:187px;width:250px;text-align:center}
.service .photo-circle{width:250px;height:250px;border:none}
.service h3{margin-top:30px;font-family:"Montserrat",Arial,sans-serif;font-weight:700;font-size:15px;color:var(--white);text-transform:uppercase}

/* works */
.works h2.section-title{position:absolute;top:1665px;width:1200px;left:0}
.works-desc{left:360px;top:1710px;width:480px;text-align:center;font-size:12px;line-height:20px;color:var(--ink)}
.work{border:1px solid var(--line)}

/* testimonials */
.testimonials{left:0;top:2365px;width:1200px;height:387px;background:var(--mint)}
.testimonials h2.section-title{position:absolute;top:40px;width:1200px}
.card{position:absolute;top:120px;height:205px;background:var(--white);border:1px solid #e3e7e4;padding:45px 32px 0 30px}
.card .quote{position:absolute;left:30px;top:-8px;width:26px;height:26px;background:var(--white);display:flex;align-items:center;justify-content:center}
.card p{font-size:11.5px;line-height:18px;color:var(--ink)}
.card .author{margin-top:22px;display:flex;align-items:center;gap:12px}
.card .avatar{width:40px;height:40px;border-radius:50%;background:linear-gradient(#c9ccd2,#8e939c)}
.card .by{font-size:9px;color:var(--muted);text-transform:uppercase}
.card .name{font-family:"Montserrat",Arial,sans-serif;font-weight:700;font-size:11px;color:var(--navy);text-transform:uppercase}

/* contact */
.talk{left:0;top:2752px;width:1200px;height:520px;background:linear-gradient(90deg,var(--navy) 0%,#1c168a 50%,var(--navy) 100%)}
.talk h2.section-title{position:absolute;top:46px;width:1200px;color:var(--white);font-size:24px}
.talk-sub{position:absolute;top:88px;width:1200px;text-align:center;font-size:10px;color:var(--white);letter-spacing:.5px;text-transform:uppercase}
.field{position:absolute;background:#e9e9ec;font-size:10px;color:#9a9ca4;padding:10px 12px}
.send-btn{left:510px;top:3150px;width:157px;height:38px}

/* footer */
.footer{left:0;top:3190px;width:1200px;height:368px;background:var(--black)}
.footer-curve{left:0;top:3150px;width:1200px;height:120px}
.fcol{top:3276px;color:#c9c9c9;font-size:11px}
.fcol h4{font-family:"Montserrat",Arial,sans-serif;font-weight:700;font-size:12px;color:var(--white);text-transform:uppercase;margin-bottom:18px}
.fcol li{list-style:none;line-height:26px;text-transform:uppercase;font-size:10px}
.fcol.services-list li{text-transform:none;font-size:11px}
.finfo{display:flex;gap:14px;align-items:flex-start;margin-bottom:26px;line-height:16px}
.socials{display:flex;gap:9px}
.socials span{width:18px;height:18px;border-radius:50%;background:#2f7fd8}
.copyright{left:0;top:3496px;width:1200px;text-align:center;font-size:10px;color:#6d6d6d}
</style>
</head>
<body>

<header>
  <div class="abs topbar"></div>
  <div class="abs brand"><span class="brand-mark"></span><span class="brand-name">Marlo Tidy Yard</span></div>
  <div class="abs contact-top" style="left:708px">
    <span class="ico"><svg width="12" height="10" viewBox="0 0 12 10"><rect x="0.5" y="0.5" width="11" height="9" fill="none" stroke="#fff"/><path d="M1 1l5 4 5-4" fill="none" stroke="#fff"/></svg></span>
    hello@marlotidyyard.net
  </div>
  <div class="abs contact-top" style="left:898px">
    <span class="ico"><svg width="12" height="12" viewBox="0 0 12 12"><path d="M2 1l2 0 1 3-1.5 1a7 7 0 003.5 3.5L8 7l3 1v2a1 1 0 01-1 1A9 9 0 011 2a1 1 0 011-1z" fill="#fff"/></svg></span>
    Call : 555-014-7720
  </div>
  <nav class="abs nav">
    <ul>
      <li class="active">Home</li><li>About Us</li><li>Services</li><li>Our Works</li><li>Clients</li><li>Contact Us</li>
    </ul>
  </nav>
</header>

<section>
  <div class="abs hero" role="img" aria-label="Bright interior room under renovation with a site worker in a yellow hard hat holding a pipe wrench and wearing a tool belt"></div>
  <div class="abs hero-arrow"></div>
  <svg class="abs" style="left:65px;top:200px" width="14" height="16" viewBox="0 0 14 16"><path d="M10 2L4 8l6 6" fill="none" stroke="#fff" stroke-width="2"/></svg>
  <h1 class="abs hero-title">Reliable. Responsive.<br>Resourceful.</h1>
  <p class="abs hero-sub">Your pet is in good hands with us! Let your favorite get the best care in our center.</p>
  <div class="abs btn hero-btn">Read More</div>
  <svg class="abs hero-curve" viewBox="0 0 1200 115" preserveAspectRatio="none">
    <path d="M0 0 Q600 140 1200 0 L1200 115 L0 115Z" fill="#fff"/>
    <path d="M150 58 Q600 120 1050 40 Q600 112 150 58Z" fill="#0e0a55"/>
  </svg>
</section>

<section>
  <h2 class="abs about-title">ABOUT <b>MARLO TIDY YARD</b></h2>
  <div class="abs about-text">
    <p>Welcome to the homepage of the veterinary practice of Dr. med. Tomas Velden. My team and I have put together information about the practice and information for patients.</p>
    <p>In addition, you can arrange appointments outside of this time with us. This is particularly recommended for predictable examinations or treatments, such as vaccinations or dressings, more extensive examinations, detailed counselling sessions or even for particularly anxious or difficult to handle animals. Please let us know at the time of appointment on the phone with just how many animals you want to come and what we can do for you, so that we can take this into account in the scheduling.</p>
    <p>Of course, we make every effort to keep appointments as precisely as possible. Please understand, however, if due to an unpredictable emergency, it may be necessary to wait. At the same time we ask you to cancel us in time if you can not make an appointment.</p>
  </div>
  <div class="abs photo-circle about-photo-lg" role="img" aria-label="Workers finishing drywall in an empty room"></div>
  <div class="abs photo-circle about-photo-sm" role="img" aria-label="Engineers in hard hats and safety vests reviewing plans under a steel frame"></div>
</section>

<section class="abs services">
  <h2 class="section-title">Our <b>Services</b></h2>
  <p class="services-desc">Lorem ipsum dolor sit amet, consectetur adipiscing elit. Earum repellat vitae fugiat voluptatum autem repudiandae rerum porro dicta, neque minima.</p>
  <div class="service" style="left:136px">
    <div class="photo-circle" style="background:radial-gradient(circle,#c9b89a,#6d6150)" role="img" aria-label="Cleaned construction interior after renovation"></div>
    <h3>Post Construction</h3>
  </div>
  <div class="service" style="left:480px">
    <div class="photo-circle" style="background:radial-gradient(circle,#c48a76,#5f5f5a)" role="img" aria-label="Pressure washing a paved surface"></div>
    <h3>Specialty Services</h3>
  </div>
  <div class="service" style="left:816px">
    <div class="photo-circle" style="background:radial-gradient(circle,#e9e6e1,#a9a49c)" role="img" aria-label="Sweeping debris in a room under construction"></div>
    <h3>Janitorial</h3>
  </div>
</section>

<section class="works">
  <h2 class="section-title">Our <b>Latest Works</b></h2>
  <p class="abs works-desc">We are proud to present to you our latest projects. Behind each one is a great team, hard work, and satisfied clients.</p>
  <div class="abs work" style="left:132px;top:1773px;width:296px;height:269px;background:linear-gradient(#f2f2f2,#d8d6d3)" role="img" aria-label="Cleaner mopping a white room"></div>
  <div class="abs work" style="left:448px;top:1773px;width:299px;height:269px;background:linear-gradient(#eef0ee,#b5c2a4)" role="img" aria-label="Cleaning crew vacuuming and wiping an apartment"></div>
  <div class="abs work" style="left:772px;top:1773px;width:298px;height:269px;background:linear-gradient(90deg,#3f4a52,#aebcc4)" role="img" aria-label="Worker steam cleaning a large window"></div>
  <div class="abs work" style="left:132px;top:2067px;width:490px;height:249px;background:linear-gradient(#9aa3a8,#7b4b3c)" role="img" aria-label="Roofers working on a tiled house roof"></div>
  <div class="abs work" style="left:635px;top:2067px;width:435px;height:249px;background:linear-gradient(#a8a49e,#5e5a55)" role="img" aria-label="Road crew in safety vests laying asphalt"></div>
</section>

<section class="abs testimonials">
  <h2 class="section-title">Client <b>Testimonials</b></h2>
  <div class="card" style="left:132px;width:286px">
    <span class="quote"><svg width="16" height="12" viewBox="0 0 16 12"><path d="M0 12V6Q0 1 6 0v2Q3 3 3 6h3v6zM9 12V6q0-5 6-6v2q-3 1-3 4h3v6z" fill="#1a1478"/></svg></span>
    <p>Industry's standard dummy text ever since the when an unknown printer took a galley of type and scrambled it to make.</p>
    <div class="author"><span class="avatar"></span><div><div class="by">By</div><div class="name">Rina Kalder</div></div></div>
  </div>
  <div class="card" style="left:450px;width:292px">
    <span class="quote"><svg width="16" height="12" viewBox="0 0 16 12"><path d="M0 12V6Q0 1 6 0v2Q3 3 3 6h3v6zM9 12V6q0-5 6-6v2q-3 1-3 4h3v6z" fill="#1a1478"/></svg></span>
    <p>Industry's standard dummy text ever since the when an unknown printer took a galley of type and scrambled it to make.</p>
    <div class="author"><span class="avatar"></span><div><div class="by">By</div><div class="name">Rina Kalder</div></div></div>
  </div>
  <div class="card" style="left:782px;width:288px">
    <span class="quote"><svg width="16" height="12" viewBox="0 0 16 12"><path d="M0 12V6Q0 1 6 0v2Q3 3 3 6h3v6zM9 12V6q0-5 6-6v2q-3 1-3 4h3v6z" fill="#1a1478"/></svg></span>
    <p>Industry's standard dummy text ever since the when an unknown printer took a galley of type and scrambled it to make.</p>
    <div class="author"><span class="avatar"></span><div><div class="by">By</div><div class="name">Rina Kalder</div></div></div>
  </div>
</section>

<section class="abs talk">
  <h2 class="section-title">Lets <b>Talk</b></h2>
  <p class="talk-sub">Tell us about your project or just say hello</p>
</section>
<div class="field" style="left:239px;top:2871px;width:341px;height:42px">Name</div>
<div class="field" style="left:613px;top:2871px;width:343px;height:42px">Phone Number</div>
<div class="field" style="left:239px;top:2943px;width:717px;height:43px">E-Mail Address</div>
<div class="field" style="left:239px;top:3013px;width:717px;height:94px">Message</div>

<footer>
  <div class="abs footer"></div>
  <svg class="abs footer-curve" viewBox="0 0 1200 120" preserveAspectRatio="none">
    <path d="M0 40 Q600 110 1200 20 L1200 120 L0 120Z" fill="#050505"/>
  </svg>
  <div class="abs btn send-btn">Send Now</div>
  <div class="abs fcol" style="left:150px">
    <h4>Quick Links</h4>
    <ul><li>Home</li><li>About Us</li><li>Our Services</li><li>Our Works</li><li>Testimonials</li><li>Contact Us</li></ul>
  </div>
  <div class="abs fcol" style="left:398px">
    <h4>Contact Us</h4>
    <div class="finfo"><svg width="10" height="14" viewBox="0 0 10 14"><path d="M5 0a5 5 0 015 5c0 4-5 9-5 9S0 9 0 5a5 5 0 015-5z" fill="#bbb"/><circle cx="5" cy="5" r="2" fill="#050505"/></svg><span>418 Orrin Lane<br>Fallow, MI 40000</span></div>
    <div class="finfo"><svg width="12" height="12" viewBox="0 0 12 12"><path d="M2 1l2 0 1 3-1.5 1a7 7 0 003.5 3.5L8 7l3 1v2a1 1 0 01-1 1A9 9 0 011 2a1 1 0 011-1z" fill="#bbb"/></svg><span>+1 555 010 482</span></div>
    <div class="finfo"><svg width="12" height="10" viewBox="0 0 12 10"><rect width="12" height="10" fill="#bbb"/><path d="M0 0l6 5 6-5" fill="none" stroke="#050505"/></svg><span>contact@marlotidyyard.com</span></div>
  </div>
  <div class="abs fcol" style="left:622px">
    <h4>Social Links</h4>
    <div class="socials"><span style="background:#3b5a9a"></span><span style="background:#2aa3e6"></span><span style="background:#d34836"></span><span style="background:#1d7ab8"></span></div>
  </div>
  <div class="abs fcol services-list" style="left:864px">
    <h4>Our Services</h4>
    <ul><li>Labour</li><li>Maintenance</li><li>Cleaning</li><li>Post Cleaning</li></ul>
  </div>
  <p class="abs copyright">©2018 MARLOTIDYYARD.com. All Rights Reserved</p>
</footer>

</body>
</html>
```